Research, Writing and Editing business needs a Business Card Design

I need a business card design for a new company based in Melbourne called The Bellwood Advisory Group. We provide research, writing and editing services. The company logo is attached, but I am open to your creative designs for business cards with the logo. As you will note, there are two potential logos. Feel free to use either of the logos.

The overall look I am hoping for is sleek, sophisticated, feminine and elegant.

Thanks in advance for your efforts.

Target Market(s)

Business professionals, academics and students

Industry/Entity Type

Business

Font styles to use
Serif
Script

Colors

Designer to choose colors to be used in the design.

Requirements
Must have
• The Bellwood Advisory Group
Dr Tessa Brennig

M: 0458 293 647
E: tessa@thebellwoodadvisorygroup.com.au
W: thebellwoodadvisorygroup.com.au
Nice to have
• Research | Writing | Editing

```html
<!DOCTYPE html>
<html lang="en">
<head>
<meta charset="utf-8">
<title>The Bellwood Advisory Group – Business Card</title>
<link rel="stylesheet" href="https://fonts.googleapis.com/css2?family=Great+Vibes&family=Didact+Gothic&family=Open+Sans:wght@700&display=swap">
<style>
  :root {
    --page-bg: #2b2b2b;
    --card-dark: #0c0c0c;
    --card-light: #f7f7f7;
    --ink: #1a1a1a;
    --ink-soft: #3a3a3a;
    --url-grey: #555555;
    --on-dark: #e6e6e6;
    --on-dark-soft: #bdbdbd;
  }
  * { box-sizing: border-box; margin: 0; padding: 0; }
  html, body { width: 1200px; height: 997px; overflow: hidden; }
  body {
    background: var(--page-bg);
    font-family: "Didact Gothic", sans-serif;
    position: relative;
  }
  .card {
    position: absolute;
    left: 290px;
    width: 620px;
    height: 379px;
    border-radius: 26px;
    box-shadow: 0 14px 30px rgba(0,0,0,0.45);
  }
  .card--back { top: 90px; background: var(--card-dark); color: var(--on-dark); }
  .card--front { top: 528px; background: var(--card-light); color: var(--ink); }

  /* back side */
  .back-brand {
    position: absolute;
    right: 56px;
    top: 150px;
    text-align: right;
  }
  .brand-line { display: flex; align-items: center; gap: 12px; justify-content: flex-end; }
  .brand-dot {
    width: 14px; height: 14px; border-radius: 50%;
    background: var(--on-dark);
  }
  .back-brand .brand-name { font-size: 24px; letter-spacing: 1px; color: var(--on-dark); }
  .services {
    margin-top: 12px;
    font-size: 17px;
    letter-spacing: 1px;
    color: var(--on-dark-soft);
  }

  /* front side */
  .front-brand {
    position: absolute;
    top: 52px;
    left: 0; right: 0;
    display: flex; justify-content: center; align-items: center; gap: 12px;
  }
  .front-brand .brand-dot { background: var(--ink); }
  .front-brand .brand-name { font-size: 24px; letter-spacing: 1px; color: var(--ink); }

  .name-row {
    position: absolute;
    top: 140px; left: 40px; right: 40px;
    display: flex; align-items: center; gap: 18px;
  }
  .rule { flex: 1; height: 2px; background: var(--ink); }
  .person-name {
    font-family: "Great Vibes", cursive;
    font-size: 44px;
    color: var(--ink);
    white-space: nowrap;
  }
  .website {
    position: absolute;
    top: 215px; left: 0; right: 0;
    text-align: center;
    font-family: "Open Sans", sans-serif;
    font-weight: 700;
    font-size: 17px;
    color: var(--url-grey);
  }
  .contact {
    position: absolute;
    top: 262px; left: 0; right: 0;
    text-align: center;
    font-size: 19px;
    line-height: 36px;
    color: var(--ink-soft);
    letter-spacing: 0.5px;
  }
</style>
</head>
<body>
  <section class="card card--back" aria-label="Card back">
    <div class="back-brand">
      <div class="brand-line">
        <span class="brand-dot"></span>
        <span class="brand-name">The Bellwood Advisory Group</span>
      </div>
      <p class="services">Research | Writing | Editing</p>
    </div>
  </section>

  <section class="card card--front" aria-label="Card front">
    <div class="front-brand">
      <span class="brand-dot"></span>
      <span class="brand-name">The Bellwood Advisory Group</span>
    </div>
    <div class="name-row">
      <span class="rule"></span>
      <h1 class="person-name">Dr Tessa Brennig</h1>
      <span class="rule"></span>
    </div>
    <p class="website">www.thebellwoodadvisorygroup.com.au</p>
    <div class="contact">
      <p class="phone">0458 293 647</p>
      <p class="email">tessa@thebellwoodadvisorygroup.com.au</p>
    </div>
  </section>
</body>
</html>
```